Visitenkarten-Design für architect i.a.
Aufgabenstellung
Logo ( Siehe Anhang)
scrinari
dessignader da construcziun aulta
maturitad professiunla
architect i.a.

```html
<!DOCTYPE html>
<html lang="rm">
<head>
<meta charset="utf-8">
<title>Torvel – Visitenkarte</title>
<link rel="stylesheet" href="https://fonts.googleapis.com/css2?family=Open+Sans:wght@300;400;600&display=swap">
<style>
  :root {
    --sky: #8fd0ec;
    --slate: #4f6a7a;
    --pale: #e3f1f9;
    --ink: #333a3f;
    --mark: #575c60;
    --paper: #ffffff;
    --ground: #ffffff;
  }
  * { box-sizing: border-box; margin: 0; padding: 0; }
  html, body { width: 1200px; height: 1200px; overflow: hidden; background: var(--ground); }
  body { font-family: "Open Sans", Arial, sans-serif; color: var(--ink); }

  .sheet { position: relative; width: 1200px; height: 1200px; }

  .card {
    position: absolute;
    top: 431px;
    width: 520px;
    height: 337px;
    background: var(--paper);
    overflow: hidden;
    box-shadow: 0 10px 14px rgba(0,0,0,0.35), 0 1px 3px rgba(0,0,0,0.2);
  }
  .card--front { left: 60px; }
  .card--back  { left: 620px; }

  .band { position: absolute; top: 54px; height: 23px; }
  .band--sky { left: 0; width: 120px; background: var(--sky); }
  .band--slate { background: var(--slate); right: 0; }
  .card--front .band--slate { left: 262px; }
  .card--back .band--slate {
    left: 271px;
    display: flex; align-items: center; justify-content: center; gap: 8px;
    color: #cfe6f2; font-size: 16px; font-weight: 400; letter-spacing: 0.5px;
  }

  .pillar {
    position: absolute; left: 436px; top: 22px; width: 35px; bottom: 0;
    background: var(--pale);
  }
  .pillar-cross {
    position: absolute; left: 436px; top: 54px; width: 35px; height: 23px;
    background: #f4f9fc;
  }

  .brand-square {
    position: absolute; top: 22px; width: 48px; height: 48px;
    background: var(--sky);
  }
  .card--front .brand-square { left: 166px; }
  .card--back .brand-square { left: 177px; }

  .wordmark {
    position: absolute; left: 62px; top: 104px;
    font-size: 62px; font-weight: 600; line-height: 1; letter-spacing: 1px;
    color: var(--mark);
  }
  .titles {
    position: absolute; left: 64px; top: 206px;
    list-style: none; font-size: 17px; line-height: 26px; color: var(--ink);
  }

  .contact {
    position: absolute; left: 71px; top: 119px;
    font-size: 18px; line-height: 26px; color: var(--ink);
  }
  .contact p { position: relative; }
  .contact .email { margin-top: 30px; font-weight: 600; }
  .icon {
    position: absolute; left: -26px; width: 17px; height: 17px;
  }
  .contact .icon { top: 4px; }
  .icon--web { position: absolute; left: 45px; top: 268px; }
</style>
</head>
<body>
<main class="sheet">

  <section class="card card--front" aria-label="Visitenkarte Vorderseite">
    <div class="band band--sky"></div>
    <div class="brand-square"></div>
    <div class="band band--slate"></div>
    <div class="pillar"></div>
    <div class="pillar-cross"></div>
    <div class="wordmark">torvel</div>
    <ul class="titles">
      <li>Scrinari</li>
      <li>Dessignader da construcziun aulta</li>
      <li>Maturitad professiunla</li>
      <li>Architect i.a.</li>
    </ul>
  </section>

  <section class="card card--back" aria-label="Visitenkarte Rückseite">
    <div class="band band--sky"></div>
    <div class="brand-square"></div>
    <div class="band band--slate">
      <svg width="16" height="16" viewBox="0 0 16 16" aria-hidden="true">
        <circle cx="8" cy="8" r="8" fill="#cfe6f2"/>
        <path d="M5.2 4.2l1.4-.3.8 1.9-.9.7c.4 1 1.2 1.8 2.2 2.2l.7-.9 1.9.8-.3 1.4c-3.3.2-6-2.5-5.8-5.8z" fill="#4f6a7a"/>
      </svg>
      <span>079 412 56 70</span>
    </div>

    <div class="contact">
      <p>Torvel Kinst</p>
      <p>
        <svg class="icon" viewBox="0 0 17 17" aria-hidden="true">
          <circle cx="8.5" cy="8.5" r="8.5" fill="#8fd0ec"/>
          <path d="M8.5 3.5a3 3 0 0 0-3 3c0 2.3 3 6 3 6s3-3.7 3-6a3 3 0 0 0-3-3z" fill="#fff"/>
          <circle cx="8.5" cy="6.5" r="1.1" fill="#8fd0ec"/>
        </svg>
        Birkenmattstrasse 12
      </p>
      <p>6010 Kriens</p>
      <p class="email">
        <svg class="icon" viewBox="0 0 17 17" aria-hidden="true">
          <circle cx="8.5" cy="8.5" r="8.5" fill="#8fd0ec"/>
          <rect x="4" y="5.5" width="9" height="6" fill="#fff"/>
          <path d="M4 5.5l4.5 3.5 4.5-3.5" stroke="#8fd0ec" stroke-width="1" fill="none"/>
        </svg>
        torvelkinst@alpnetz.ch
      </p>
    </div>
    <svg class="icon icon--web" viewBox="0 0 17 17" aria-hidden="true">
      <circle cx="8.5" cy="8.5" r="8.5" fill="#8fd0ec"/>
      <path d="M8.5 4l4.5 4h-1.3v4.5H5.3V8H4z" fill="#fff"/>
    </svg>
  </section>

</main>
</body>
</html>
```